Business Card Design Project

I need a template business card for a web design / software company called

"Design marrowind"

we specialize in propelling archaic paper-based processes into the fore of the 21st century with web based solutions, graphical interfaces, graphic design outsourcing, automation software deployments, database design and development, segmentation of data and preservation of data integrity.

http://lexicon.wordquarry.com/browse/phenomena
British Dictionary definitions for phenomena

phenomena
/fɪˈnɒmɪnə/
noun
1.
a plural of phenomenon
phenomenon
/fɪˈnɒmɪnən/
noun (pl) -ena (-ɪnə), -enons
1.
anything that can be perceived as an occurrence or fact by the senses
2.
any remarkable occurrence or person
3.
(philosophy)

the object of perception, experience, etc
(in the writings of Brell) a thing as it appears and is interpreted in perception and reflection, as distinguished from its real nature as a thing-in-itself Compare noumenon
"

I am very open minded here I am letting you take the design and run with it...

good luck

Target Market(s)

Professional companies, small business in western speaking countries in need of collating design capabilities for web pages, web stores, graphic design or software development projects

Industry/Entity Type

Graphic Design

Colors

Designer to choose colors to be used in the design.

Requirements
Must have
• Designed in Adobe Illustrator

```html
<!DOCTYPE html>
<html lang="en">
<head>
<meta charset="utf-8">
<title>Design marrowind — Business Cards</title>
<link rel="stylesheet" href="https://fonts.googleapis.com/css2?family=Questrial&display=swap">
<style>
  :root {
    --backdrop: #1c1c1c;
    --card-light: #ffffff;
    --card-dark: #000000;
    --ink-dark: #1a1a1a;
    --ink-grey: #5a5a5a;
    --ink-light: #e6e6e6;
    --mark-grey: #8a8a8a;
  }
  * { margin: 0; padding: 0; box-sizing: border-box; }
  html, body {
    width: 1200px;
    height: 900px;
    overflow: hidden;
    background: var(--backdrop);
    font-family: "Questrial", sans-serif;
  }
  .card-set {
    position: absolute;
    inset: 0;
    display: flex;
    justify-content: center;
    align-items: center;
    gap: 80px;
  }
  .card {
    position: relative;
    width: 300px;
    height: 525px;
    overflow: hidden;
  }
  .card--light { background: var(--card-light); }
  .card--dark { background: var(--card-dark); }

  /* Contact block, set upside down at the top of the light card */
  .contact {
    position: absolute;
    top: 28px;
    right: 34px;
    transform: rotate(180deg);
    transform-origin: center;
    color: var(--ink-grey);
    font-size: 12px;
    line-height: 1.55;
    text-align: left;
  }
  .contact__name {
    font-size: 15px;
    color: var(--ink-dark);
    margin-top: 8px;
  }

  /* Wordmark, running up the card's long edge */
  .wordmark {
    position: absolute;
    display: flex;
    align-items: center;
    gap: 14px;
    transform: rotate(-90deg);
    transform-origin: left top;
    white-space: nowrap;
  }
  .card--light .wordmark { left: 120px; top: 470px; }
  .card--dark .wordmark { left: 135px; top: 480px; }
  .wordmark__square {
    width: 26px;
    height: 26px;
    flex: none;
  }
  .card--light .wordmark__square { background: var(--ink-dark); }
  .card--dark .wordmark__square { background: var(--ink-light); }
  .wordmark__name {
    font-size: 30px;
    letter-spacing: 0.5px;
  }
  .card--light .wordmark__name { color: var(--ink-dark); }
  .card--dark .wordmark__name { color: var(--ink-light); }
</style>
</head>
<body>
  <main class="card-set">
    <section class="card card--light" aria-label="Card front with contact details">
      <div class="contact">
        <p>M: 0400 000 000</p>
        <p>email: info@designmarrowind.com</p>
        <p>web: designmarrowind.com</p>
        <p class="contact__name">Tom Harlow</p>
      </div>
      <div class="wordmark">
        <span class="wordmark__square"></span>
        <span class="wordmark__name">Design marrowind</span>
      </div>
    </section>

    <section class="card card--dark" aria-label="Card back with wordmark">
      <div class="wordmark">
        <span class="wordmark__square"></span>
        <span class="wordmark__name">Design marrowind</span>
      </div>
    </section>
  </main>
</body>
</html>
```